Cobalt Peak Vending Needs a Promotional Flyer

Design a one page, one sided 8 1/2" x 11" flyer that can be handed out to potential customers. Please keep printing efficiencies in mind. See attached old flyers and company website (cobaltpeakvending.com) for reference of services. I have also attached our current logo.

```html
<!DOCTYPE html>
<html lang="en">
<head>
<meta charset="utf-8">
<title>Cobalt Peak Vending – Flyer</title>
<link href="https://fonts.googleapis.com/css2?family=Poppins:wght@400;500;600;700;800&display=swap" rel="stylesheet">
<style>
:root{
  --navy:#0f2a3a;
  --blue:#1a9ad6;
  --ink:#1f2a33;
  --white:#ffffff;
  --stage:#939393;
}
*{margin:0;padding:0;box-sizing:border-box}
html,body{width:812px;height:1200px;overflow:hidden;background:var(--stage);font-family:'Poppins',sans-serif;color:var(--ink)}
.flyer{position:absolute;left:0;top:75px;width:812px;height:1050px;background:var(--white);overflow:hidden}
.abs{position:absolute}
.hero-blue{left:479px;top:0;width:333px;height:125px;background:var(--blue)}
.hero-navy{left:0;top:0}
.hero-photo{left:433px;top:119px;width:343px;height:287px;border-radius:4px;background:linear-gradient(90deg,#2a2d31 0%,#3b3f44 48%,#d8321f 52%,#e84a2a 100%)}
.badge{left:536px;top:30px;width:94px;height:94px;border-radius:50%;background:var(--navy);display:flex;align-items:center;justify-content:center}
.badge-inner{width:74px;height:74px;border-radius:50%;background:var(--white);display:flex;flex-direction:column;align-items:center;justify-content:center;line-height:1}
.badge-num{font-size:22px;font-weight:700;color:var(--navy)}
.badge-years{font-size:9px;font-weight:700;color:var(--blue);margin-top:2px}
.badge-exp{font-size:6px;font-weight:600;color:var(--navy);letter-spacing:.5px;margin-top:2px}
.welcome{left:91px;top:142px;font-size:22px;font-weight:700;color:#333;letter-spacing:.3px}
.brand{left:88px;top:170px;font-size:41px;font-weight:700;color:var(--navy);line-height:1.02;letter-spacing:-.5px}
.hero-phone{left:86px;top:268px;font-size:24px;font-weight:700;color:#333;display:flex;align-items:center;gap:8px}
.why{left:47px;top:418px;width:718px;height:188px;background:var(--navy);color:var(--white)}
.why-title{left:22px;top:22px;font-size:20px;font-weight:400;white-space:nowrap}
.why-title b{color:var(--blue);font-weight:700}
.why-item{position:absolute;display:flex;gap:9px;align-items:flex-start;font-size:10.6px;line-height:1.22}
.why-icon{flex:none;width:23px;height:23px;border-radius:50%;border:1.5px solid var(--blue);background:#1d3f55;display:flex;align-items:center;justify-content:center;margin-top:-1px}
.section-title{left:67px;top:615px;font-size:25px;font-weight:800;color:var(--navy);letter-spacing:-.2px;white-space:nowrap}
.tag{background:var(--blue);color:var(--white);font-weight:700;text-transform:uppercase;padding:0 6px;line-height:1;white-space:nowrap}
.tag-vending{left:69px;top:655px;width:180px;height:42px;font-size:16.5px;padding:4px 6px;line-height:1}
.tag-coffee{left:69px;top:766px;width:170px;height:19px;font-size:16.5px;padding:1px 9px}
.tag-pantry{left:424px;top:655px;width:177px;height:19px;font-size:16.5px;padding:1px 5px}
.tag-micro{left:424px;top:801px;width:177px;height:19px;font-size:16.5px;padding:1px 4px}
.photo{border:1.5px solid var(--ink)}
.photo-vending{left:256px;top:655px;width:125px;height:93px;background:linear-gradient(90deg,#fff 30%,#1c3e7a 32%,#2a5aa0 68%,#fff 70%)}
.photo-coffee{left:256px;top:768px;width:125px;height:93px;background:radial-gradient(ellipse at 62% 50%,#f2efe9 0 28%,#6b3f22 40%,#3a2010 100%)}
.photo-pantry{left:617px;top:656px;width:126px;height:93px;background:linear-gradient(90deg,#5a3a25 0%,#7b5236 60%,#d9dde0 78%,#5a3a25 100%)}
.photo-micro{left:617px;top:801px;width:126px;height:93px;background:linear-gradient(90deg,#c8a46c 0%,#b23a2a 35%,#d9b47a 55%,#2f5ea8 100%)}
.bullets{list-style:none;font-size:10.5px;font-weight:600;color:var(--navy);line-height:13.5px}
.bullets li{position:relative;padding-left:12px}
.bullets li::before{content:"";position:absolute;left:1px;top:4.5px;width:6px;height:6px;border-radius:50%;background:var(--blue)}
.nowrap li{white-space:nowrap}
.ticks{display:grid;font-size:10px;font-weight:400;color:#333;line-height:13.4px;white-space:nowrap}
.ticks span::before{content:"✓ ";font-size:8px}
.ticks span:empty::before{content:""}
.footer-navy{left:0;top:0}
.call-label{left:75px;top:977px;font-size:15.5px;font-weight:600;color:var(--white);letter-spacing:.3px}
.call-phone{left:72px;top:994px;font-size:27px;font-weight:700;color:var(--white);display:flex;align-items:center;gap:8px}
.contact{font-size:12px;color:var(--navy);line-height:14.5px;display:flex;gap:7px;align-items:flex-start;white-space:nowrap}
</style>
</head>
<body>
<main class="flyer">
  <!-- hero -->
  <div class="abs hero-blue"></div>
  <svg class="abs hero-navy" width="812" height="420" aria-hidden="true">
    <polygon points="669,13 812,0 812,408 669,392" fill="#0f2a3a"/>
  </svg>
  <div class="abs hero-photo" role="img" aria-label="Photo of a snack vending machine beside a red cold-drink vending machine"></div>
  <div class="abs badge"><div class="badge-inner"><span class="badge-num">30+</span><span class="badge-years">YEARS</span><span class="badge-exp">EXPERIENCE</span></div></div>

  <div class="abs welcome">WELCOME TO</div>
  <div class="abs brand">COBALT PEAK<br>VENDING</div>
  <div class="abs hero-phone">
    <svg width="16" height="16" viewBox="0 0 24 24" aria-hidden="true"><path fill="#1a9ad6" d="M6.6 10.8a15.1 15.1 0 0 0 6.6 6.6l2.2-2.2a1 1 0 0 1 1-.25 11.4 11.4 0 0 0 3.6.57 1 1 0 0 1 1 1V20a1 1 0 0 1-1 1A17 17 0 0 1 3 4a1 1 0 0 1 1-1h3.5a1 1 0 0 1 1 1c0 1.25.2 2.45.57 3.57a1 1 0 0 1-.25 1z"/></svg>
    555-014-2278
  </div>

  <!-- why choose -->
  <section class="abs why">
    <h2 class="abs why-title">Why Choose Our <b>Vending Machine Services?</b></h2>
    <div class="why-item" style="left:22px;top:60px;width:240px"><span class="why-icon"><svg width="12" height="12" viewBox="0 0 12 12"><circle cx="6" cy="6.5" r="4.5" fill="none" stroke="#fff" stroke-width="1.2"/><path d="M6 4v3l2 1" stroke="#fff" stroke-width="1.2" fill="none"/></svg></span><span>Our warehouse is just minutes<br>away so we can get there quickly<br>if a problem should arise.</span></div>
    <div class="why-item" style="left:22px;top:112px;width:240px"><span class="why-icon"><svg width="12" height="12" viewBox="0 0 12 12"><rect x="3" y="1.5" width="6" height="9" fill="none" stroke="#fff" stroke-width="1.2"/><path d="M4.5 4h3M4.5 6h3M4.5 8h3" stroke="#fff"/></svg></span><span>We are a small company<br>that is BIG on service.</span></div>
    <div class="why-item" style="left:22px;top:146px;width:240px"><span class="why-icon"><svg width="12" height="12" viewBox="0 0 12 12"><circle cx="6" cy="4" r="2" fill="#fff"/><path d="M2 10.5a4 4 0 0 1 8 0z" fill="#fff"/></svg></span><span style="margin-top:4px">Customer Service is our priority.</span></div>
    <div class="why-item" style="left:264px;top:62px;width:200px"><span class="why-icon"><svg width="12" height="12" viewBox="0 0 12 12"><path d="M6 10.5 1.8 6.3a2.4 2.4 0 0 1 4.2-2.8 2.4 2.4 0 0 1 4.2 2.8z" fill="#fff"/></svg></span><span>We are Owner-Operators so<br>we truly CARE about our<br>customers.</span></div>
    <div class="why-item" style="left:264px;top:113px;width:200px"><span class="why-icon"><svg width="12" height="12" viewBox="0 0 12 12"><circle cx="6" cy="5" r="3" fill="none" stroke="#fff" stroke-width="1.2"/><path d="M4.5 8.5 4 11l2-1 2 1-.5-2.5" fill="#fff"/></svg></span><span>We are also trained to fix<br>many problems on the spot.</span></div>
    <div class="why-item" style="left:480px;top:62px;width:225px"><span class="why-icon"><svg width="12" height="12" viewBox="0 0 12 12"><circle cx="6" cy="6" r="4" fill="none" stroke="#fff" stroke-width="1.2"/><path d="M4 6.2 5.5 7.5 8 4.8" stroke="#fff" stroke-width="1.2" fill="none"/></svg></span><span>We will supply machines<br>to your facility.</span></div>
    <div class="why-item" style="left:480px;top:100px;width:230px"><span class="why-icon"><svg width="12" height="12" viewBox="0 0 12 12"><path d="M2 10V5h2v5M5 10V3h2v7M8 10V6h2v4" fill="#fff"/></svg></span><span>Your employees can choose what<br>types of snacks and drinks they<br>would like to see in the machines.</span></div>
  </section>

  <!-- services -->
  <h2 class="abs section-title">COBALT PEAK SUPERIOR SERVICE</h2>

  <h3 class="abs tag tag-vending">Vending Machine<br>Services</h3>
  <div class="abs photo photo-vending" role="img" aria-label="Photo of a blue cold-drink vending machine"></div>
  <ul class="abs bullets nowrap" style="left:69px;top:702px">
    <li>Reliability</li><li>Variety &amp; Convenience</li><li>Zero Cost to You</li><li>Quality</li>
  </ul>

  <h3 class="abs tag tag-coffee">Coffee Service</h3>
  <div class="abs photo photo-coffee" role="img" aria-label="Photo of a cup of coffee on a saucer with coffee beans"></div>
  <ul class="abs bullets nowrap" style="left:69px;top:791px">
    <li>Reliability</li><li>Our Coffee Selection</li>
  </ul>
  <div class="abs ticks" style="left:82px;top:818px;grid-template-columns:102px 70px">
    <span>Summit Roast</span><span>Elkhorn</span>
    <span>Daybreak Donuts</span><span>Stanfords</span>
    <span>Polar Ridge</span><span>Fairbrook</span>
    <span>Hearthstone House</span><span></span>
  </div>
  <ul class="abs bullets nowrap" style="left:69px;top:876px">
    <li>Tea and other Tasty Hot Beverages</li><li>Coffee Accessories</li>
  </ul>
  <div class="abs ticks" style="left:82px;top:905px;grid-template-columns:94px 80px">
    <span>Coffee Pots</span><span>Sleeves</span>
    <span>Filters</span><span>Napkins</span>
    <span>Cups</span><span>Sugar</span>
    <span>Stirrers</span><span>Sweet-Lite</span>
  </div>
  <div class="abs ticks" style="left:266px;top:907px">
    <span>Evenly</span><span>Liquid Creamers</span><span>flavored and regular</span>
  </div>

  <h3 class="abs tag tag-pantry">Pantry Service</h3>
  <div class="abs photo photo-pantry" role="img" aria-label="Photo of an office pantry with wooden snack shelves and a drinks cooler"></div>
  <ul class="abs bullets" style="left:424px;top:677px;width:190px">
    <li>A Snack Time Oasis in Your Workspace</li><li>Tailored to Your Tastes</li><li>Healthy Choices, Happy Teams</li><li>Seamless Restocking and Management</li><li>Flexible and Hassle-Free</li><li>Enhancing Workplace Culture</li>
  </ul>

  <h3 class="abs tag tag-micro">Micro-Market</h3>
  <div class="abs photo photo-micro" role="img" aria-label="Photo of micro-market shelves stocked with snacks"></div>
  <ul class="abs bullets" style="left:424px;top:823px;width:190px">
    <li>Experience Unmatched Convenience</li><li>Tailored to Your Taste</li><li>Seamless and Secure Transactions</li><li>Freshness Guaranteed</li><li>Smart Inventory Management</li><li>Promoting Workplace Wellbeing</li>
  </ul>

  <!-- footer -->
  <svg class="abs footer-navy" width="812" height="1050" aria-hidden="true">
    <polygon points="0,971 306,971 336,1050 0,1050" fill="#0f2a3a"/>
    <polygon points="306,971 311,971 344,1047 812,1047 812,1050 339,1050" fill="#1a9ad6"/>
  </svg>
  <div class="abs call-label">CALL US AT</div>
  <div class="abs call-phone">
    <svg width="17" height="17" viewBox="0 0 24 24" aria-hidden="true"><path fill="#1a9ad6" d="M6.6 10.8a15.1 15.1 0 0 0 6.6 6.6l2.2-2.2a1 1 0 0 1 1-.25 11.4 11.4 0 0 0 3.6.57 1 1 0 0 1 1 1V20a1 1 0 0 1-1 1A17 17 0 0 1 3 4a1 1 0 0 1 1-1h3.5a1 1 0 0 1 1 1c0 1.25.2 2.45.57 3.57a1 1 0 0 1-.25 1z"/></svg>
    555-014-2278
  </div>
  <div class="abs contact" style="left:339px;top:990px">
    <svg width="14" height="16" viewBox="0 0 14 16" aria-hidden="true"><path d="M7 15S2 9.5 2 6a5 5 0 0 1 10 0c0 3.5-5 9-5 9z" fill="none" stroke="#1a9ad6" stroke-width="1.5"/><circle cx="7" cy="6" r="1.8" fill="#1a9ad6"/></svg>
    <span>1480 Meadowlark Ave, Unit 212,<br>Brookfield Ridge, IL 60999</span>
  </div>
  <div class="abs contact" style="left:564px;top:990px">
    <svg width="14" height="14" viewBox="0 0 14 14" aria-hidden="true"><circle cx="7" cy="7" r="6" fill="none" stroke="#1a9ad6" stroke-width="1.3"/><ellipse cx="7" cy="7" rx="2.6" ry="6" fill="none" stroke="#1a9ad6" stroke-width="1"/><path d="M1 7h12" stroke="#1a9ad6"/></svg>
    <span>cobaltpeakvending.com</span>
  </div>
</main>
</body>
</html>
```